Maple Dawn Confections. We need a website as delcious as our chocolate.

I need a website to promote our humble chocolate business. We our proud of are chocolate because we use only our favorite ingredients. We believe in originality and complete enjoyment of our chocolates. I am looking for a sleek and smooth website. I would like to see typical pages such as contact information and an intro. I would like to have a product page, which can be easily updated with photos of new chocolate. I would also like to see a page where we can educate customers about chocolate. This might be tricky but I would like our customers to leave the site knowing they are getting great chocolate! I have a logo and general color scheme, which I will try to upload somewhere. I looking for an original and exciting website.
Updates

Websites we like:

1. http://www.corvel-amand.example/ (looks really good)

2. http://www.tilvarocacao.example/

uploaded logo !

Target Market(s)

People who enjoy chocolate.

Industry/Entity Type

Business

Requirements
Must have
• User Friendly
Page were pictures of new chocolate can be easily updated.

Nice to have
• Calming and appetizing music
Section where recent tweets can show up on the site.

```html
<!DOCTYPE html>
<html lang="en">
<head>
<meta charset="utf-8">
<title>Maple Dawn Confections</title>
<link rel="stylesheet" href="https://fonts.googleapis.com/css2?family=Playball&family=Open+Sans:ital,wght@0,400;0,600;0,700;1,400;1,700&display=swap">
<style>
:root{
  --cocoa-night:#2c0a10;
  --cocoa-deep:#3a0e16;
  --rose:#e27fa8;
  --rose-strong:#d4669a;
  --rose-active:#a0506e;
  --caramel:#d9a07a;
  --caramel-dark:#7a4a35;
  --linen:#e2c69e;
  --linen-dark:#cfae82;
  --panel:#5a3c40;
  --panel-edge:#3a1a1e;
  --footer:#4a3232;
  --ink:#2b0a0e;
  --white:#ffffff;
  --script:"Playball",cursive;
  --sans:"Open Sans",sans-serif;
}
*{box-sizing:border-box;margin:0;padding:0}
html,body{width:1112px;height:1200px;overflow:hidden;background:var(--linen)}
body{font-family:var(--sans);color:var(--ink)}
.page{position:relative;width:1112px;height:1200px;overflow:hidden;background:var(--linen)}
.abs{position:absolute}

/* top bar */
.topbar{left:0;top:0;width:1112px;height:90px;background:var(--cocoa-night)}
.top-links{right:80px;top:18px;font-size:13.5px;font-weight:600;color:var(--white);letter-spacing:.1px}
.login-field{top:46px;height:27px;width:120px;background:linear-gradient(#d8c8c0,#b8a49c);border:2px solid #8a7068;color:#5a2a30;font-size:12.5px;padding:4px 10px}
.login-btn{left:990px;top:44px;width:68px;height:30px;border:2px solid var(--rose);background:var(--cocoa-deep);color:var(--white);font-size:12.5px;text-align:center;line-height:26px}

/* hero */
.hero{left:0;top:90px;width:1112px;height:688px;background:
  radial-gradient(ellipse 38% 22% at 62% 48%,#f6c8a6 0%,#d79a74 35%,transparent 60%),
  radial-gradient(ellipse 60% 42% at 60% 50%,#a05e42 0%,#6e3424 45%,transparent 75%),
  radial-gradient(ellipse 80% 70% at 55% 45%,#8a4a34 0%,#4a1e16 70%),
  #3e1812}
.logo{left:74px;top:118px;width:220px;font-family:var(--script);color:var(--rose-strong);font-size:30px;line-height:1.05}

.nav-item{top:170px;width:131px;height:46px;background:var(--cocoa-night);border:2px solid var(--rose);color:var(--white);font-family:var(--script);font-size:16.5px;text-align:center;line-height:42px}
.nav-item.is-active{background:var(--rose-active)}
.dropdown{left:481px;top:217px;width:131px}
.dropdown-item{height:29px;background:var(--cocoa-night);border:2px solid var(--rose);border-top-width:1px;color:var(--white);font-family:var(--script);font-size:14px;text-align:center;line-height:26px}

.welcome{left:91px;top:335px;width:487px;height:173px;background:rgba(58,22,22,.6);border:1px solid rgba(0,0,0,.25);color:var(--white)}
.welcome h1{font-family:var(--script);font-weight:400;color:var(--rose-strong);font-size:27px;text-align:center;margin:28px 0 4px -70px;color:#e88ab8}
.welcome .quote{font-style:italic;font-size:13.5px;line-height:14px;padding:0 20px 0 26px;text-indent:34px;letter-spacing:.3px}
.welcome .cite{font-size:10.5px;color:#f2a0c4;margin:14px 0 0 122px;line-height:13px;letter-spacing:.3px}

.cta{left:180px;top:520px;width:304px;height:46px;background:linear-gradient(#3a0e16,#240609);border:2px solid var(--rose);color:var(--white);font-family:var(--script);font-size:22px;text-align:center;line-height:42px}

/* popular products */
.popular{left:86px;top:639px;width:941px;height:241px;background:var(--panel);border:3px solid var(--panel-edge);border-radius:3px}
.popular-title{left:114px;top:656px;width:187px;height:46px;background:var(--cocoa-night);border:2px solid var(--rose);color:var(--white);font-family:var(--script);font-size:22px;text-align:center;line-height:42px}
.card{top:717px;width:209px;height:148px;background:linear-gradient(#ffffff 40%,#f0e2e6);border-radius:5px}
.card h3{position:absolute;left:13px;top:12px;font-family:var(--script);font-weight:400;font-size:18px;color:var(--ink);white-space:nowrap}
.card .thumb{position:absolute;left:24px;top:42px;width:88px;height:64px;border-radius:30px}
.card .price{position:absolute;right:18px;top:91px;font-size:12.5px;color:var(--ink)}
.card .price b{font-size:14px;font-weight:600}
.card .add{position:absolute;right:16px;top:109px;width:80px;height:25px;background:var(--cocoa-deep);color:var(--white);font-size:11.5px;font-weight:600;text-align:center;line-height:25px;border-radius:2px}
.thumb-heart{background:radial-gradient(circle at 60% 50%,#e0201e 0%,#b51414 45%,#6a2a1c 75%,transparent 78%)}
.thumb-peanut{background:radial-gradient(ellipse at 50% 55%,#6b2a18 0%,#3e140c 55%,transparent 72%)}
.thumb-box{background:radial-gradient(ellipse at 45% 50%,#c89a68 0%,#8a6040 50%,transparent 72%);border-radius:8px}

.arrow{top:743px;width:48px;height:52px;background:linear-gradient(#6a4a4c,#4a2a2e);border:2px solid var(--panel-edge);border-radius:3px}

/* testimonials & contact */
.section-title{font-family:var(--script);font-size:22px;color:var(--ink);font-weight:400}
.testimonials{left:99px;top:909px;width:580px}
.testimonials h2{margin-left:37px}
.testimonial{margin-top:14px}
.testimonial p{font-style:italic;font-weight:700;font-size:13.2px;line-height:14px;text-indent:30px}
.testimonial cite{display:block;font-style:normal;font-size:11px;font-weight:600;margin-left:3px;line-height:14px}
.divider{left:719px;top:935px;width:2px;height:118px;background:linear-gradient(transparent,#b08a68 20%,#b08a68 80%,transparent)}
.contact{left:751px;top:910px}
.contact h2{margin-left:19px}
.contact-row{position:absolute;left:0;display:flex;align-items:center;gap:14px;white-space:nowrap}
.icon{width:35px;height:33px;border-radius:6px}
.icon-phone{background:linear-gradient(#7ad45a,#3f9a2a)}
.icon-social-a{background:linear-gradient(#5a78b8,#2f4c8c)}
.icon-social-b{background:linear-gradient(#9adcf4,#4aa8d8)}
.phone-number{font-size:22px;font-weight:600;letter-spacing:.8px}
.social-label{font-size:13px;font-weight:600}

/* footer */
.footer{left:0;top:1096px;width:1112px;height:104px;background:repeating-linear-gradient(90deg,#4e3434 0 2px,#463030 2px 4px),var(--footer)}
.footer-links{left:0;top:1164px;width:1112px;text-align:center;font-size:13px;color:#eea6c2;font-weight:600}
</style>
</head>
<body>
<div class="page">

  <header class="topbar abs"></header>
  <nav class="top-links abs">Home / Chocolate / Customer service / About us / FAQ / Contact us</nav>
  <div class="login-field abs" style="left:738px">Email adress</div>
  <div class="login-field abs" style="left:862px">Password</div>
  <div class="login-btn abs">Login</div>

  <section class="hero abs" role="img" aria-label="Swirl of melted chocolate in glossy caramel and dark cocoa tones"></section>

  <div class="logo abs">Maple Dawn<br>Confections</div>

  <nav aria-label="Main">
    <div class="nav-item abs" style="left:329px">About Us</div>
    <div class="nav-item abs is-active" style="left:481px">Chocolate</div>
    <div class="nav-item abs" style="left:631px">Our products</div>
    <div class="nav-item abs" style="left:782px">Specials</div>
    <div class="nav-item abs" style="left:928px">Contact us</div>
    <div class="dropdown abs">
      <div class="dropdown-item">Lorem Ipsum</div>
      <div class="dropdown-item">Lorem Ipsum</div>
      <div class="dropdown-item">Lorem Ipsum</div>
    </div>
  </nav>

  <section class="welcome abs">
    <h1>Welcome!</h1>
    <p class="quote">"Chocolate is a divine, celestial drink, the sweat of the stars, the vital seed, divine nectar, the drink of the gods, panacea and universal medicine."</p>
    <p class="cite">(Orsino Valdetti, quoted by Marcelo Durrano,<br>Spanish army surgeon,1796)</p>
  </section>

  <div class="cta abs">View all products</div>

  <section class="popular abs" aria-label="Popular products"></section>
  <h2 class="popular-title abs" style="font-weight:400">Popular products</h2>

  <div class="arrow abs" style="left:37px">
    <svg width="44" height="48" viewBox="0 0 44 48"><path d="M28 12 L14 24 L28 36" fill="none" stroke="#fff" stroke-width="3"/></svg>
  </div>
  <div class="arrow abs" style="left:1033px">
    <svg width="44" height="48" viewBox="0 0 44 48"><path d="M16 12 L30 24 L16 36" fill="none" stroke="#fff" stroke-width="3"/></svg>
  </div>

  <article class="card abs" style="left:109px">
    <h3>The Valentine's Heart</h3>
    <div class="thumb thumb-heart" role="img" aria-label="Red heart-shaped chocolate box"></div>
    <div class="price">Price: <b>25&amp;</b></div>
    <div class="add">Add to Cart</div>
  </article>
  <article class="card abs" style="left:340px">
    <h3>Chocolate Peanuts</h3>
    <div class="thumb thumb-peanut" role="img" aria-label="Pile of chocolate-coated peanuts"></div>
    <div class="price">Price: <b>19 &amp;</b></div>
    <div class="add">Add to Cart</div>
  </article>
  <article class="card abs" style="left:570px">
    <h3>Dark Chocolate Assort Box</h3>
    <div class="thumb thumb-box" role="img" aria-label="Open gift box of dark chocolates"></div>
    <div class="price">Price: <b>25&amp;</b></div>
    <div class="add">Add to Cart</div>
  </article>
  <article class="card abs" style="left:799px">
    <h3>The Valentine's Heart</h3>
    <div class="thumb thumb-heart" role="img" aria-label="Red heart-shaped chocolate box"></div>
    <div class="price">Price: <b>25&amp;</b></div>
    <div class="add">Add to Cart</div>
  </article>

  <section class="testimonials abs">
    <h2 class="section-title">Testimonials</h2>
    <div class="testimonial">
      <p>"Chocolate is a divine, celestial drink, the sweat of the stars, the vital seed, divine nectar, the drink of the gods, panacea and universal medicine."</p>
      <cite>(Orsino Valdetti, quoted by Marcelo Durrano, Spanish army surgeon,1796)</cite>
    </div>
    <div class="testimonial">
      <p>Chocolate is a divine, celestial drink, the sweat of the stars, the vital seed, divine nectar, the drink of the gods, panacea and universal medicine."</p>
      <cite>(Orsino Valdetti, quoted by Marcelo Durrano, Spanish army surgeon,1796)</cite>
    </div>
  </section>

  <div class="divider abs"></div>

  <section class="contact abs">
    <h2 class="section-title">Contact with us</h2>
    <div class="contact-row" style="top:44px">
      <div class="icon icon-phone">
        <svg width="35" height="33" viewBox="0 0 35 33"><path d="M11 7 c2 0 3 4 3 5 s-2 2-2 3 c1 3 4 6 7 7 c1 0 2-2 3-2 s5 1 5 3 s-2 4-4 4 c-8 0-16-8-16-16 c0-2 2-4 4-4z" fill="#fff"/></svg>
      </div>
      <span class="phone-number">318 602 49</span>
    </div>
    <div class="contact-row" style="top:81px">
      <div class="icon icon-social-a"></div>
      <span class="social-label">Like us on Chatterly</span>
    </div>
    <div class="contact-row" style="top:114px">
      <div class="icon icon-social-b"></div>
      <span class="social-label">Follow us on Chirpline</span>
    </div>
  </section>

  <footer class="footer abs"></footer>
  <nav class="footer-links abs">Home / Chocolate / Customer service / Dealer Login / About us / FAQ / Contact us</nav>

</div>
</body>
</html>
```